Hi! We require a design for business cards for directors and head teachers of an international daycare for children 0 - 9. We are family-owned, -operated and -oriented. We have six locations, looking to franchise. Our USPs are: 1) Flexibility 2) Quality teachers 3) International culture 4) Best nutrition We are quality teachers and professional caretakers, but with creativity and personality! Business cards should be playful (but no Comic Sans or baby hand prints), colorful (but no rainbows), and have some breathing space. It should be obvious from the business card that we're a daycare. In 2020 we'll be launching our new website based on this design: https://plomvane.io/47K2RQLWZTD The font in the new website will be Houschka (medium, demibold, bold). We will keep our current logo, included in the files here. There are also screenshots of some designs we like. Show us your best! :)

Industry/Entity Type

Childcare

Contact Information for Business Card

Lotte de Vries-Bakhuis
Communications Wizard
Poppel Hoek International Daycare
Kastanjeweg 47 B, 2316 KR Leiden
www.poppelhoek.nl
+31 647315082

Font styles to use
Serif
Sans Serif

Colors

Designer to choose colors to be used in the design.

Requirements
Must have
• Color

```html
<!DOCTYPE html>
<html lang="en">
<head>
<meta charset="utf-8">
<title>Poppel Hoek – Business Card</title>
<link rel="stylesheet" href="https://fonts.googleapis.com/css2?family=Raleway:wght@600;700&family=Open+Sans:wght@400&display=swap">
<style>
  :root {
    --stage: #ecebec;
    --card: #ffffff;
    --ink: #111111;
    --pink: #ef7fb2;
    --pink-soft: #f4a9c9;
    --sky: #a9dcf1;
  }
  html, body {
    margin: 0;
    padding: 0;
    overflow: hidden;
  }
  body {
    width: 1200px;
    height: 1010px;
    background: var(--stage);
    position: relative;
  }
  .card {
    position: absolute;
    left: 318px;
    width: 567px;
    box-sizing: border-box;
  }
  .card--front {
    top: 187px;
    height: 328px;
    overflow: hidden;
  }
  .card-pattern {
    position: absolute;
    inset: 0;
    background: linear-gradient(120deg, var(--pink) 0%, var(--pink-soft) 40%, var(--sky) 100%);
  }
  .brand {
    position: absolute;
    left: 160px;
    top: 92px;
    display: flex;
    flex-direction: column;
    gap: 14px;
  }
  .brand-line {
    display: flex;
    align-items: center;
    gap: 12px;
    font-family: "Raleway", sans-serif;
    font-weight: 700;
    font-size: 50px;
    line-height: 56px;
    letter-spacing: 12px;
    color: var(--ink);
    text-transform: uppercase;
  }
  .brand-line--second {
    margin-left: 80px;
  }
  .brand-dot {
    width: 14px;
    height: 14px;
    border-radius: 50%;
    background: var(--ink);
  }
  .card--back {
    top: 534px;
    height: 322px;
    background: var(--card);
    text-align: center;
    color: var(--ink);
    font-family: "Open Sans", sans-serif;
    font-size: 15.5px;
    line-height: 20px;
  }
  .person-name {
    position: absolute;
    top: 56px;
    left: 0;
    right: 0;
    margin: 0;
    font-family: "Raleway", sans-serif;
    font-weight: 600;
    font-size: 17px;
    letter-spacing: 0.3px;
    text-transform: uppercase;
  }
  .person-role {
    position: absolute;
    top: 80px;
    left: 0;
    right: 0;
    margin: 0;
    font-family: "Raleway", sans-serif;
    font-weight: 600;
    font-size: 14.5px;
  }
  .company {
    position: absolute;
    top: 119px;
    left: 0;
    right: 0;
    margin: 0;
  }
  .website {
    position: absolute;
    top: 177px;
    left: 0;
    right: 0;
    margin: 0;
  }
  .phone {
    position: absolute;
    top: 213px;
    left: 0;
    right: 0;
    margin: 0;
  }
  .contact-icons {
    position: absolute;
    top: 254px;
    left: 0;
    right: 0;
    display: flex;
    justify-content: center;
    gap: 5px;
  }
  .contact-icons svg {
    width: 18px;
    height: 18px;
    fill: var(--ink);
  }
</style>
</head>
<body>

  <section class="card card--front">
    <div class="card-pattern" role="img" aria-label="Playful pattern of overlapping pink, blue, yellow and green triangles"></div>
    <div class="brand">
      <span class="brand-line">Poppel</span>
      <span class="brand-line brand-line--second"><span class="brand-dot"></span>Hoek</span>
    </div>
  </section>

  <section class="card card--back">
    <h1 class="person-name">Lotte de Vries-Bakhuis</h1>
    <p class="person-role">Communications Wizard</p>
    <p class="company">Poppel Hoek International Daycare<br>Kastanjeweg 47 B, 2316 KR Leiden</p>
    <p class="website">www.poppelhoek.nl</p>
    <p class="phone">+31 647 315 082</p>
    <div class="contact-icons">
      <svg viewBox="0 0 24 24" aria-label="Address">
        <path d="M12 1a7 7 0 0 0-7 7c0 5 7 12 7 12s7-7 7-12a7 7 0 0 0-7-7zm0 9.5a2.5 2.5 0 1 1 0-5 2.5 2.5 0 0 1 0 5z"/>
        <rect x="5" y="21" width="14" height="2" rx="1"/>
      </svg>
      <svg viewBox="0 0 24 24" aria-label="Website">
        <path d="M12 2a10 10 0 1 0 0 20 10 10 0 0 0 0-20zm6.9 6h-2.9a15 15 0 0 0-1.4-3.6A8 8 0 0 1 18.9 8zM12 4c.8 1.2 1.5 2.5 1.9 4h-3.8c.4-1.5 1.1-2.8 1.9-4zM4.3 14a8 8 0 0 1 0-4h3.3a16 16 0 0 0 0 4H4.3zm.8 2h2.9c.3 1.3.8 2.5 1.4 3.6A8 8 0 0 1 5.1 16zM8 8H5.1a8 8 0 0 1 4.3-3.6C8.8 5.5 8.3 6.7 8 8zm4 12c-.8-1.2-1.5-2.5-1.9-4h3.8c-.4 1.5-1.1 2.8-1.9 4zm2.3-6H9.7a14 14 0 0 1 0-4h4.6a14 14 0 0 1 0 4zm.3 5.6c.6-1.1 1.1-2.3 1.4-3.6h2.9a8 8 0 0 1-4.3 3.6zm1.8-5.6a16 16 0 0 0 0-4h3.3a8 8 0 0 1 0 4h-3.3z"/>
      </svg>
      <svg viewBox="0 0 24 24" aria-label="Phone">
        <path d="M12 5c-4.5 0-8.5 1.2-10 3v3h5V9c1.5-.5 3.2-.7 5-.7s3.5.2 5 .7v2h5V8c-1.5-1.8-5.5-3-10-3z"/>
        <path d="M7 12l-3 7h16l-3-7H7zm5 5.5a2.5 2.5 0 1 1 0-5 2.5 2.5 0 0 1 0 5z"/>
      </svg>
    </div>
  </section>

</body>
</html>
```